Fitness industry business card

Dear Designers,

I'm looking to have a business card designed that will appeal to affluent wealthy clients, I would
To have high end clean cut luxurious understated minimalistic feel to the business cards.

I look forward to the first draft of design ideas. I will send the info that I would like to have on the cards shortly.

Best Wishes
Marika

```html
<!DOCTYPE html>
<html lang="en">
<head>
<meta charset="utf-8">
<title>MK-FORM Business Card</title>
<link href="https://fonts.googleapis.com/css2?family=Michroma&display=swap" rel="stylesheet">
<style>
  :root {
    --backdrop: #262526;
    --card-dark: #3b3e43;
    --card-light: #474a50;
    --card-deep: #303236;
    --band: #f4f4f4;
    --ink-dark: #141414;
    --ink-light: #e9e9ea;
  }
  * { box-sizing: border-box; margin: 0; padding: 0; }
  html, body {
    width: 1200px;
    height: 900px;
    overflow: hidden;
    background: var(--backdrop);
  }
  .canvas {
    width: 1200px;
    height: 900px;
    display: flex;
    align-items: center;
    justify-content: center;
    gap: 80px;
    font-family: "Michroma", sans-serif;
  }
  .card {
    position: relative;
    width: 380px;
    height: 640px;
    background:
      repeating-linear-gradient(180deg, rgba(255,255,255,0.025) 0 1px, transparent 1px 3px),
      linear-gradient(160deg, var(--card-light) 0%, var(--card-dark) 45%, var(--card-deep) 100%);
    box-shadow: 0 18px 40px rgba(0,0,0,0.45);
  }
  .card-back {
    display: flex;
    align-items: center;
    justify-content: center;
  }
  .brand-tag {
    background: var(--band);
    color: var(--ink-dark);
    padding: 14px 26px;
    font-size: 20px;
    letter-spacing: 1px;
  }
  .title-band {
    position: absolute;
    left: 0;
    right: 0;
    top: 120px;
    background: var(--band);
    color: var(--ink-dark);
    padding: 16px 24px;
    text-align: right;
    font-size: 15px;
    line-height: 1.45;
    letter-spacing: 0.5px;
  }
  .details {
    position: absolute;
    left: 54px;
    top: 300px;
    color: var(--ink-light);
  }
  .holder-name {
    font-size: 18px;
    letter-spacing: 3px;
    margin-bottom: 20px;
  }
  .contact-list { list-style: none; }
  .contact-item {
    display: flex;
    align-items: center;
    gap: 10px;
    font-size: 12px;
    letter-spacing: 0.5px;
    margin-bottom: 12px;
  }
  .contact-item svg { flex: none; }
  .contact-item.handle { margin-left: 34px; }
</style>
</head>
<body>
<main class="canvas">
  <section class="card card-back">
    <div class="brand-tag">MK-FORM</div>
  </section>

  <section class="card card-front">
    <div class="title-band">AESTHETICS AND BODY<br>TRANSFORMATION SPECIALIST</div>
    <div class="details">
      <h1 class="holder-name">MARIKA KOVALENKO</h1>
      <ul class="contact-list">
        <li class="contact-item">
          <svg width="14" height="14" viewBox="0 0 14 14" aria-hidden="true">
            <rect x="3.5" y="1" width="7" height="12" rx="1.2" fill="none" stroke="#e9e9ea" stroke-width="1.3"/>
            <line x1="6" y1="11" x2="8" y2="11" stroke="#e9e9ea" stroke-width="1.2"/>
          </svg>
          (0044) 70215-48390
        </li>
        <li class="contact-item">
          <svg width="14" height="14" viewBox="0 0 14 14" aria-hidden="true">
            <rect x="1" y="3" width="12" height="8" fill="none" stroke="#e9e9ea" stroke-width="1.3"/>
            <polyline points="1,3 7,8 13,3" fill="none" stroke="#e9e9ea" stroke-width="1.3"/>
          </svg>
          mkformcoaching@mailbox.com
        </li>
        <li class="contact-item handle">
          <svg width="14" height="14" viewBox="0 0 14 14" aria-hidden="true">
            <rect x="1.5" y="1.5" width="11" height="11" rx="2" fill="#e9e9ea"/>
          </svg>
          MKFORM
        </li>
      </ul>
    </div>
  </section>
</main>
</body>
</html>
```